TriVex Business Card Design - double sided -plumbing local plumbing company

We have a Plumbing company where the design was create through Sketch Hive. We would now like a business card designed as well. We want it to be in the colour version of the logo.

Details below for the card.

Phone Number: 0438 615 247
Email: info@trivexplumbing.example.au
Website: https://trivexplumbing.example.au
We really want a sophisticated design that stand out from the other- informative and timeless.

Target Market(s)

local Canberra market

Industry/Entity Type

Plumbing, gas fitting, hot water

Contact Information for Business Card

Phone number, email, logo and "Supplying all your heating, cooling and hot water needs"

Requirements
Must have
• bust be colourful, must also be though about it being printed on a magnet. must Vex with the logo - I dont want the logo and information chucked onto a white canvas I would prefer it to be smooth and look purposeful

```html
<!DOCTYPE html>
<html lang="en">
<head>
<meta charset="utf-8">
<title>TriVex Plumbing – Business Card</title>
<link rel="stylesheet" href="https://fonts.googleapis.com/css2?family=Arimo:wght@400;700&display=swap">
<style>
  :root {
    --navy: #011a38;
    --navy-mid: #0b2d5c;
    --sky: #0fa3e3;
    --sky-deep: #0288cf;
    --gold: #f2a531;
    --white: #ffffff;
    --backdrop: #e4e4e4;
  }
  * { box-sizing: border-box; margin: 0; padding: 0; }
  html, body { width: 1200px; height: 801px; overflow: hidden; }
  body {
    background: var(--backdrop);
    font-family: "Arimo", Arial, sans-serif;
    display: flex;
    align-items: center;
    justify-content: center;
    gap: 40px;
  }
  .card {
    position: relative;
    width: 540px;
    height: 309px;
    background: var(--navy);
    border: 2px solid var(--gold);
    overflow: hidden;
  }
  .card__art { position: absolute; inset: 0; width: 100%; height: 100%; }

  /* Front */
  .front__tab {
    position: absolute; top: 0; right: 18px;
    width: 14px; height: 34px; background: var(--gold);
  }
  .front__person {
    position: absolute; top: 22px; right: 42px; text-align: right;
  }
  .front__name {
    font-weight: 700; font-size: 19px; letter-spacing: 0.5px; text-transform: uppercase;
  }
  .front__name-first { color: var(--sky); }
  .front__name-last { color: var(--gold); }
  .front__role { color: var(--white); font-size: 13px; margin-top: 3px; }

  .brand {
    position: absolute; left: 52px; top: 118px;
    color: var(--sky); font-weight: 700;
  }
  .brand__name { font-size: 50px; line-height: 1; letter-spacing: 1px; }
  .brand__sub { font-size: 20px; letter-spacing: 9px; margin-top: 4px; text-transform: uppercase; }

  .contact {
    position: absolute; right: 22px; top: 196px;
    list-style: none; text-align: right; color: var(--navy);
    font-size: 12.5px; line-height: 19px;
  }
  .contact__item { display: flex; justify-content: flex-end; align-items: center; gap: 7px; }
  .contact__icon { width: 12px; height: 12px; flex: none; }

  /* Back */
  .back__brand {
    position: absolute; left: 110px; bottom: 52px;
    color: var(--sky); font-weight: 700;
  }
  .back__brand .brand__name { font-size: 28px; }
  .back__brand .brand__sub { font-size: 11px; letter-spacing: 5px; margin-top: 2px; }
  .back__tagline {
    position: absolute; left: 240px; bottom: 60px;
    color: var(--white); font-weight: 700; font-size: 12.5px;
    line-height: 17px; text-transform: uppercase; letter-spacing: 0.3px;
  }
</style>
</head>
<body>

  <section class="card card--front" aria-label="Business card front">
    <svg class="card__art" viewBox="0 0 540 309" preserveAspectRatio="none" aria-hidden="true">
      <defs>
        <linearGradient id="skyFill" x1="0" y1="0" x2="1" y2="1">
          <stop offset="0" stop-color="#1cb0ee"/>
          <stop offset="1" stop-color="#0288cf"/>
        </linearGradient>
      </defs>
      <path d="M70,309 C250,300 290,215 335,150 S440,82 540,76 L540,309 Z" fill="url(#skyFill)"/>
      <path d="M0,296 C215,290 265,200 315,130 S430,62 540,56" fill="none" stroke="var(--gold)" stroke-width="6"/>
      <path d="M180,280 C270,250 300,190 320,160" fill="none" stroke="var(--gold)" stroke-width="1.5"/>
    </svg>

    <div class="front__tab"></div>
    <div class="front__person">
      <p class="front__name"><span class="front__name-first">Marcus</span> <span class="front__name-last">Reilly</span></p>
      <p class="front__role">Manager</p>
    </div>

    <div class="brand">
      <p class="brand__name">TriVex</p>
      <p class="brand__sub">Plumbing</p>
    </div>

    <ul class="contact">
      <li class="contact__item">0438 615 247
        <svg class="contact__icon" viewBox="0 0 12 12" aria-hidden="true"><path d="M3 1 L5 3.5 L4 5 C4.6 6.4 5.6 7.4 7 8 L8.5 7 L11 9 L9.5 11 C5 10.5 1.5 7 1 2.5 Z" fill="var(--navy)"/></svg>
      </li>
      <li class="contact__item">info@trivexplumbing.example.au
        <svg class="contact__icon" viewBox="0 0 12 12" aria-hidden="true"><rect x="0.8" y="2.5" width="10.4" height="7" fill="none" stroke="var(--navy)" stroke-width="1.2"/><path d="M0.8 2.5 L6 6.5 L11.2 2.5" fill="none" stroke="var(--navy)" stroke-width="1.2"/></svg>
      </li>
      <li class="contact__item">www.trivexplumbing.example.au
        <svg class="contact__icon" viewBox="0 0 12 12" aria-hidden="true"><circle cx="6" cy="6" r="5" fill="none" stroke="var(--navy)" stroke-width="1.2"/><ellipse cx="6" cy="6" rx="2.2" ry="5" fill="none" stroke="var(--navy)" stroke-width="1"/><path d="M1 6 H11 M2 3.5 H10 M2 8.5 H10" stroke="var(--navy)" stroke-width="1"/></svg>
      </li>
    </ul>
  </section>

  <section class="card card--back" aria-label="Business card back">
    <svg class="card__art" viewBox="0 0 540 309" preserveAspectRatio="none" role="img" aria-label="Embossed repeating brand pattern across the card">
      <defs>
        <linearGradient id="patternFill" x1="0" y1="0" x2="1" y2="0.6">
          <stop offset="0" stop-color="#021c3d"/>
          <stop offset="1" stop-color="#0b2d5c"/>
        </linearGradient>
      </defs>
      <rect width="540" height="309" fill="url(#patternFill)"/>
    </svg>

    <div class="back__brand">
      <p class="brand__name">TriVex</p>
      <p class="brand__sub">Plumbing</p>
    </div>
    <p class="back__tagline">Supplying all your heating<br>cooling and hot water needs</p>
  </section>

</body>
</html>
```